Business Card Design for Kidvale (Hires out childrens play areas)

Looking to have a business card designed for a company we just bought. The company rents out childrens play areas.

I have uploaded a couple of examples of the kind of business card style I like. Here are two more examples:

https://quorvastudio.nz/project/bright-romp-branding/
https://imgvaultcdn.com/design_img/8841052/302917/302917_5518203_8841052_b73e19a2_image.jpg

I think a white card will be best due to all the colours in the logo.

Size we require: 3.75" x 2.25" (horizontally orientated) with a 0.125" bleed

Uploaded is two versions of our logo.

Details for the card:
1. My name: Liam Verster
2. Title: Managing Director
3. Phone no: 021 563 417
4. Email: liam@kidvale.co.nz
5. URL: www.kidvale.co.nz
6. Address:
PO Box 318625
Fernlea, Auckland

Let me know if you need anything else.

Target Market(s)

Hospitals, doctors surgeries, bed shops, etc.

Contact Information for Business Card

Details for the card:
1. My name: Liam Verster
3. Phone no: 021 563 417
5. URL: www.kidvale.co.nz
6. Address:
PO Box 318625
Fernlea, Auckland

Requirements
Should not have
• Not too busy.

```html
<!DOCTYPE html>
<html lang="en">
<head>
<meta charset="utf-8">
<title>Kidvale Business Card</title>
<link href="https://fonts.googleapis.com/css2?family=Montserrat:wght@400;600;800&display=swap" rel="stylesheet">
<style>
  :root {
    --canvas-bg: #d4d5d6;
    --card-white: #fbfbfb;
    --ink: #4a4a4a;
    --name-orange: #ec5a24;
    --rule-blue: #2a6fd1;
    --rule-purple: #8a3bb5;
    --icon-green: #3fae3a;
    --brand-blue: #1f5fcf;
    --back-blue: #2b5fc9;
    --glow: #ffffff;
  }
  * { margin: 0; padding: 0; box-sizing: border-box; }
  html, body { width: 1200px; height: 900px; overflow: hidden; }
  body {
    background: var(--canvas-bg);
    font-family: "Montserrat", sans-serif;
    display: flex;
    align-items: center;
    justify-content: center;
    gap: 60px;
  }
  .card {
    width: 480px;
    height: 288px;
    position: relative;
    overflow: hidden;
    box-shadow: 0 6px 18px rgba(0,0,0,0.12);
  }
  .card-front {
    background: var(--card-white);
    display: flex;
    align-items: center;
    justify-content: center;
    gap: 26px;
  }
  .contact {
    text-align: right;
    color: var(--ink);
    font-size: 11.5px;
    line-height: 1.55;
  }
  .contact-name {
    color: var(--name-orange);
    font-weight: 600;
    font-size: 17px;
    letter-spacing: 0.5px;
    text-transform: uppercase;
    margin-bottom: 2px;
  }
  .contact-group + .contact-group { margin-top: 10px; }
  .contact-line { display: flex; justify-content: flex-end; align-items: center; gap: 6px; }
  .contact-line svg { width: 11px; height: 11px; flex: none; }
  .rules {
    display: flex;
    flex-direction: column;
    gap: 6px;
    align-self: center;
  }
  .rule { width: 1.5px; height: 34px; }
  .rule-blue { background: var(--rule-blue); }
  .rule-purple { background: var(--rule-purple); }
  .brand {
    display: flex;
    align-items: center;
    gap: 8px;
  }
  .brand-dot {
    width: 16px; height: 16px; border-radius: 50%;
    background: var(--brand-blue);
  }
  .brand-name {
    font-weight: 800;
    font-size: 30px;
    color: var(--brand-blue);
  }
  .card-back {
    background: radial-gradient(ellipse 55% 45% at 50% 50%, var(--glow) 0%, var(--glow) 35%, #c9d8f3 60%, var(--back-blue) 100%);
    display: flex;
    align-items: center;
    justify-content: center;
  }
  .card-back .brand-name { font-size: 46px; }
  .card-back .brand-dot { width: 24px; height: 24px; }
</style>
</head>
<body>
  <section class="card card-front" aria-label="Business card front">
    <div class="contact">
      <div class="contact-group">
        <p class="contact-name">Liam Verster</p>
        <p>Managing Director</p>
        <p>PO Box 318625</p>
        <p>Fernlea, Auckland</p>
      </div>
      <div class="contact-group">
        <p class="contact-line">021 563 417
          <svg viewBox="0 0 24 24" aria-hidden="true"><path fill="var(--icon-green)" d="M6.6 10.8a15 15 0 0 0 6.6 6.6l2.2-2.2a1 1 0 0 1 1-.25 11.4 11.4 0 0 0 3.6.57 1 1 0 0 1 1 1V20a1 1 0 0 1-1 1A17 17 0 0 1 3 4a1 1 0 0 1 1-1h3.5a1 1 0 0 1 1 1c0 1.25.2 2.45.57 3.6a1 1 0 0 1-.25 1z"/></svg>
        </p>
        <p class="contact-line">liam@kidvale.co.nz
          <svg viewBox="0 0 24 24" aria-hidden="true"><rect x="2" y="5" width="20" height="14" rx="2" fill="var(--icon-green)"/><path d="M3 6l9 7 9-7" fill="none" stroke="#fff" stroke-width="2"/></svg>
        </p>
        <p>www.kidvale.co.nz</p>
      </div>
    </div>
    <div class="rules" aria-hidden="true">
      <span class="rule rule-blue"></span>
      <span class="rule rule-purple"></span>
      <span class="rule rule-blue"></span>
    </div>
    <div class="brand">
      <span class="brand-dot" aria-hidden="true"></span>
      <span class="brand-name">Kidvale</span>
    </div>
  </section>

  <section class="card card-back" aria-label="Business card back">
    <div class="brand">
      <span class="brand-dot" aria-hidden="true"></span>
      <span class="brand-name">Kidvale</span>
    </div>
  </section>
</body>
</html>
```